Redgum Wrecking P/L business card

I already have a EPS logo design that I wish to use however, the company is a demolition company based on the Central Coast of NSW Australia. The company is called "Redgum Wrecking P/L".

We offer demolition services such as Residential, Commercial, Civil, Asbestos removal, Excavation and Tree removal that are required to be displayed on the rear of the business card.

We currently have 4 personnel that require business cards with their specific contact details.

The logo is mid blue on a white background and the remainder is black text on a whiter card.

The eps logo supplied should only be displayed as a logo without the text.

Target Market(s)

People, governments, companies requiring demolition services on the east coast of NSW, specifically Central Coast, Sydney and Newcastle locations.

Industry/Entity Type

Business

Contact Information for Business Card

There are four cards required
First card:
Martin Ellory
Operations Director
Mobile No. 0451 872164
E: info@redgumwreck.example.com.au
www.redgumwreck.example.com.au
Second card:
Peter Hollis
Project Director
Company Mobile: 0451 872164
Personal Mobile: 0426 158 309
www.redgumwreck.example.com.au
Third card:
Simon Brady
Project Director
Company Mobile: 0451 872 164
Personal Mobile: 0433 917 482
www.redgumwreck.example.com.au
Fourth card:
Lewis Thornby
General Manager
Personal Mobile: 0447 261 835
www.redgumwreck.example.com.au

Font styles to use
Other font styles liked:
• Helvetica

Colors
33a6d7

Requirements
Must have
• The RW logo (without the text of Redgum Wrecking)
Horizontal layout with logo on top left hand corner
Services provision on the rear of the card
Nice to have
• Logo on top left corner
Text should be something like Helvetica
Should not have
• Do not include the text that is incorporated in the EPS file I sent ….just the logo

```html
<!DOCTYPE html>
<html lang="en">
<head>
<meta charset="utf-8">
<title>Redgum Wrecking P/L – Business Card</title>
<link href="https://fonts.googleapis.com/css2?family=Mulish:wght@300;400;600;700&display=swap" rel="stylesheet">
<style>
  :root {
    --brand: #33a6d7;
    --brand-deep: #2a9bbf;
    --brand-back: #3cc3d2;
    --card-white: #ffffff;
    --ink: #2b2b2b;
    --stage: #e9e8e6;
    --on-brand: #ffffff;
  }
  * { margin: 0; padding: 0; box-sizing: border-box; }
  html, body {
    width: 1200px; height: 800px; overflow: hidden;
    background: var(--stage);
    font-family: "Mulish", Helvetica, Arial, sans-serif;
  }
  .stage {
    position: relative; width: 1200px; height: 800px;
  }
  .card {
    position: absolute; top: 250px;
    width: 525px; height: 300px;
    box-shadow: 0 6px 18px rgba(0,0,0,0.18);
    overflow: hidden;
  }

  /* ---------- Rear ---------- */
  .card-back {
    left: 45px;
    background: var(--brand-back);
    color: var(--on-brand);
  }
  .card-back .services {
    position: absolute; top: 26px; left: 30px;
    list-style: none;
    font-size: 13px; font-weight: 400;
    letter-spacing: 0.3px; text-transform: uppercase;
    line-height: 22px;
  }
  .card-back .services li::before {
    content: ""; display: inline-block;
    width: 6px; height: 6px; margin-right: 8px;
    background: rgba(255,255,255,0.75);
    vertical-align: middle; position: relative; top: -1px;
  }
  .card-back .rule {
    position: absolute; left: 0; right: 0; top: 168px;
    height: 2px; background: rgba(20,120,140,0.35);
  }
  .card-back .company {
    position: absolute; left: 28px; top: 196px;
    text-transform: uppercase;
  }
  .card-back .company-main {
    display: block;
    font-size: 38px; font-weight: 300; letter-spacing: 2px; line-height: 42px;
  }
  .card-back .company-sub {
    display: block;
    font-size: 15px; font-weight: 300; letter-spacing: 10px; margin-top: 4px;
  }

  /* ---------- Front ---------- */
  .card-front {
    left: 630px;
    background: var(--card-white);
  }
  .card-front .brand-name {
    position: absolute; left: 40px; top: 34px;
    font-size: 22px; font-weight: 600; color: var(--brand);
    letter-spacing: 0.5px;
  }
  .card-front .brand-rule {
    position: absolute; left: 0; top: 74px;
    width: 210px; height: 2px; background: var(--brand);
  }
  .card-front .person {
    position: absolute; right: 26px; top: 128px;
    text-align: right; text-transform: uppercase; color: var(--brand-deep);
  }
  .card-front .person-name {
    font-size: 22px; font-weight: 400; letter-spacing: 1.5px; line-height: 26px;
  }
  .card-front .person-role {
    font-size: 11px; font-weight: 700; letter-spacing: 0.8px; margin-top: 4px;
  }
  .card-front .accent-bar {
    position: absolute; right: 0; top: 128px;
    width: 12px; height: 48px; background: var(--brand-deep);
  }
  .card-front .contacts {
    position: absolute; left: 30px; bottom: 26px;
    list-style: none; font-size: 13px; color: var(--ink); line-height: 21px;
  }
  .card-front .contacts li { display: flex; align-items: center; }
  .card-front .contacts svg { width: 12px; height: 12px; margin-right: 10px; flex: none; }
</style>
</head>
<body>
<main class="stage">

  <section class="card card-back" aria-label="Business card rear">
    <ul class="services">
      <li>Residential</li>
      <li>Commercial</li>
      <li>Civil</li>
      <li>Asbestos Removal</li>
      <li>Excavation and Tree Removal</li>
    </ul>
    <div class="rule"></div>
    <h1 class="company">
      <span class="company-main">Redgum</span>
      <span class="company-sub">Wrecking</span>
    </h1>
  </section>

  <section class="card card-front" aria-label="Business card front">
    <div class="brand-name">Redgum Wrecking</div>
    <div class="brand-rule"></div>

    <div class="person">
      <div class="person-name">Martin Ellory</div>
      <div class="person-role">Operations Director</div>
    </div>
    <div class="accent-bar"></div>

    <ul class="contacts">
      <li>
        <svg viewBox="0 0 12 12" aria-hidden="true"><rect width="12" height="12" rx="2" fill="#33a6d7"/><rect x="4" y="2.5" width="4" height="7" rx="0.8" fill="none" stroke="#fff" stroke-width="1"/></svg>
        0451 872 164
      </li>
      <li>
        <svg viewBox="0 0 12 12" aria-hidden="true"><rect width="12" height="12" rx="2" fill="#33a6d7"/><rect x="2.5" y="3.5" width="7" height="5" fill="none" stroke="#fff" stroke-width="1"/><path d="M2.5 3.5 L6 6.5 L9.5 3.5" fill="none" stroke="#fff" stroke-width="1"/></svg>
        info@redgumwreck.example.com.au
      </li>
      <li>
        <svg viewBox="0 0 12 12" aria-hidden="true"><rect width="12" height="12" rx="2" fill="#33a6d7"/><circle cx="6" cy="6" r="3.3" fill="none" stroke="#fff" stroke-width="1"/><path d="M2.7 6 H9.3 M6 2.7 V9.3" stroke="#fff" stroke-width="0.8"/></svg>
        www.redgumwreck.example.com.au
      </li>
    </ul>
  </section>

</main>
</body>
</html>
```